Home Multi-Service Company Website

I currently have only a landing page but am looking for someone to build out a nice, modern looking website that will cover multiple services we offer like Landscape Lighting, Gutter Cleaning, Holiday Lighting, Window Cleaning, Insulation Services like Blow In and Removal, Blower Door Tests, Rodent Exclusion and Trapping and others. We would also like our Holiday lighting category to have links to a separate page for franchise opportunities.

Home

Serif
Sans Serif

• A modern and organized look. Detailed information regarding each service provided by our company.
• We are a service company so would like to see options to link reviews from plimbo and maybe some nice pictures of people at home. We would like the color to match our logo as well.

```html
<!DOCTYPE html>
<html lang="en">
<head>
<meta charset="utf-8">
<title>Brightway Home Services</title>
<link href="https://fonts.googleapis.com/css2?family=Poppins:wght@500;600;700;800&family=IBM+Plex+Sans:wght@400;500&display=swap" rel="stylesheet">
<style>
:root{
  --navy:#2f3146;
  --navy-deep:#24263a;
  --white:#ffffff;
  --text:#33354a;
}
*{margin:0;padding:0;box-sizing:border-box}
html,body{width:1200px;height:3138px;overflow:hidden;background:var(--white)}
body{position:relative;font-family:"IBM Plex Sans",sans-serif;color:var(--text)}

.site-header{position:absolute;top:0;left:0;width:1200px;height:77px;background:var(--white)}
.brand{position:absolute;left:133px;top:26px;display:flex;align-items:center;gap:9px;font-family:"Poppins",sans-serif;font-weight:700;font-size:21px;color:var(--navy);line-height:1}
.brand-mark{width:18px;height:18px;background:var(--navy)}
.main-nav{position:absolute;right:132px;top:0;height:77px;display:flex;align-items:center;gap:46px}
.main-nav a{font-family:"Poppins",sans-serif;font-weight:600;font-size:14px;color:var(--navy);text-decoration:none}

.hero{position:absolute;top:77px;left:0;width:1200px;height:607px;
  background:
    radial-gradient(ellipse 260px 140px at 28% 62%,rgba(214,190,120,.55),transparent 70%),
    radial-gradient(ellipse 220px 120px at 72% 70%,rgba(200,170,100,.5),transparent 70%),
    radial-gradient(ellipse 300px 160px at 50% 22%,rgba(150,180,70,.55),transparent 70%),
    radial-gradient(ellipse 200px 300px at 90% 30%,rgba(30,60,25,.7),transparent 70%),
    radial-gradient(ellipse 180px 260px at 8% 40%,rgba(170,150,70,.5),transparent 70%),
    linear-gradient(180deg,#3f5a1e 0%,#587a2a 35%,#5a6a2c 60%,#2d3a1a 100%)}
.hero-content{position:absolute;top:0;left:0;width:100%;text-align:center;color:var(--white)}
.hero-title{position:absolute;top:190px;width:100%;font-family:"Poppins",sans-serif;font-weight:700;font-size:49px;letter-spacing:-0.5px;text-shadow:0 2px 6px rgba(0,0,0,.55)}
.hero-sub{position:absolute;top:259px;width:100%;font-size:22px;text-shadow:0 1px 4px rgba(0,0,0,.7)}
.hero-btn{position:absolute;top:315px;left:526px;width:148px;height:46px;border:2px solid var(--white);display:flex;align-items:center;justify-content:center;font-family:"Poppins",sans-serif;font-weight:600;font-size:17px;color:var(--white);text-decoration:none}
.hero-dots{position:absolute;top:544px;left:562px;display:flex;gap:10px;align-items:center}
.hero-dots span{width:7px;height:7px;border-radius:50%;background:var(--white)}
.hero-dots .active{width:11px;height:11px;background:transparent;border:2px solid var(--white)}

.section-title{position:absolute;width:1200px;text-align:center;font-family:"Poppins",sans-serif;font-weight:700;font-size:24px;color:var(--navy)}
.services-title{top:732px}
.service-card{position:absolute;width:302px}
.service-photo{width:302px;height:249px}
.service-name{text-align:center;font-family:"Poppins",sans-serif;font-weight:600;font-size:17px;color:var(--navy);margin-top:16px}
.view-all{position:absolute;left:767px;top:1110px;width:302px;height:249px;
  background:
    radial-gradient(ellipse 110px 70px at 30% 55%,rgba(110,120,90,.6),transparent 70%),
    radial-gradient(ellipse 120px 80px at 75% 35%,rgba(90,100,80,.5),transparent 70%),
    linear-gradient(135deg,#3a4540,#2f3550);
  display:flex;align-items:center;justify-content:center;font-family:"Poppins",sans-serif;font-weight:600;font-size:18px;color:var(--white);text-decoration:none}

.welcome{position:absolute;top:1453px;left:0;width:1200px;height:552px;
  background:
    radial-gradient(ellipse 180px 200px at 88% 40%,rgba(110,120,150,.55),transparent 70%),
    radial-gradient(ellipse 150px 170px at 72% 45%,rgba(225,215,200,.7),transparent 70%),
    radial-gradient(ellipse 220px 150px at 68% 82%,rgba(70,85,110,.55),transparent 70%),
    radial-gradient(ellipse 130px 110px at 14% 82%,rgba(190,140,90,.55),transparent 70%),
    radial-gradient(ellipse 260px 180px at 60% 20%,rgba(160,175,130,.45),transparent 70%),
    linear-gradient(90deg,#b7b6ac 0%,#c6c3b6 40%,#d3d0c4 60%,#b0b0aa 100%)}
.welcome-text{position:absolute;left:133px;top:73px;width:370px;color:var(--white)}
.welcome-kicker{font-family:"Poppins",sans-serif;font-weight:700;font-size:22px;line-height:1.1}
.welcome-title{font-family:"Poppins",sans-serif;font-weight:700;font-size:34px;line-height:1.25;white-space:nowrap}
.welcome-body{margin-top:22px;font-size:19.5px;line-height:25.6px}

.reviews-title{top:2057px}
.review-card{position:absolute;width:294px;text-align:center}
.review-photo{width:294px;height:198px}
.review-name{font-family:"Poppins",sans-serif;font-weight:600;font-size:17px;color:var(--navy);margin-top:26px}
.review-text{font-size:14.5px;line-height:19.4px;margin-top:12px;padding:0 20px;color:var(--text)}

.cta{position:absolute;top:2549px;left:0;width:1200px;height:430px;
  background:
    radial-gradient(ellipse 500px 90px at 45% 60%,rgba(70,72,80,.55),transparent 70%),
    radial-gradient(ellipse 200px 120px at 5% 40%,rgba(70,80,60,.6),transparent 70%),
    linear-gradient(180deg,#303646 0%,#262a35 50%,#1d1f28 100%)}
.cta-title{position:absolute;top:146px;width:100%;text-align:center;font-family:"Poppins",sans-serif;font-weight:700;font-size:32px;color:var(--white);letter-spacing:-0.5px}
.cta-link{position:absolute;top:218px;width:100%;text-align:center;font-size:21px;color:var(--white);text-decoration:none;display:block}

.site-footer{position:absolute;top:2979px;left:0;width:1200px;height:159px;background:var(--navy)}
.footer-nav{position:absolute;top:50px;width:100%;display:flex;justify-content:center;gap:40px}
.footer-nav a{font-family:"Poppins",sans-serif;font-weight:600;font-size:14px;color:var(--white);text-decoration:none}
.copyright{position:absolute;top:101px;width:100%;text-align:center;font-size:12px;color:var(--white)}
</style>
</head>
<body>

<header class="site-header">
  <div class="brand"><span class="brand-mark"></span>Brightway Home Services</div>
  <nav class="main-nav">
    <a href="#">HOME</a><a href="#">ABOUT US</a><a href="#">SERVICES</a><a href="#">BLOG</a><a href="#">CONTACT US</a>
  </nav>
</header>

<section class="hero" role="img" aria-label="Evening garden with winding paths lit by landscape lights">
  <div class="hero-content">
    <h1 class="hero-title">LANDSCAPE LIGHTING</h1>
    <p class="hero-sub">Lorem Ipsum is simply dummy text of the printing</p>
    <a class="hero-btn" href="#">READ MORE</a>
    <div class="hero-dots"><span></span><span></span><span class="active"></span><span></span><span></span></div>
  </div>
</section>

<h2 class="section-title services-title">OUR SERVICES</h2>

<div class="service-card" style="left:133px;top:795px">
  <div class="service-photo" role="img" aria-label="Garden path lights among plants" style="background:radial-gradient(ellipse 60px 50px at 27% 45%,rgba(230,235,220,.7),transparent 70%),radial-gradient(ellipse 45px 40px at 74% 25%,rgba(220,230,210,.55),transparent 70%),linear-gradient(135deg,#2a3a12,#5d7a2a 55%,#8a6b4a)"></div>
  <p class="service-name">Landscape Lighting</p>
</div>
<div class="service-card" style="left:451px;top:795px">
  <div class="service-photo" role="img" aria-label="Worker on a ladder cleaning a roof gutter" style="background:radial-gradient(ellipse 70px 90px at 78% 55%,rgba(40,100,190,.8),transparent 70%),radial-gradient(ellipse 120px 60px at 35% 25%,rgba(90,90,90,.6),transparent 70%),linear-gradient(135deg,#6e6e6a,#9aa08a 50%,#c8c4b8)"></div>
  <p class="service-name">Gutter Cleaning</p>
</div>
<div class="service-card" style="left:767px;top:795px">
  <div class="service-photo" role="img" aria-label="Colourful holiday string lights on wood" style="background:radial-gradient(circle at 25% 30%,rgba(230,60,60,.55),transparent 25%),radial-gradient(circle at 70% 55%,rgba(60,200,120,.45),transparent 25%),radial-gradient(circle at 40% 80%,rgba(240,190,60,.45),transparent 25%),radial-gradient(circle at 85% 20%,rgba(80,150,230,.45),transparent 22%),linear-gradient(135deg,#3a2418,#5a3a26 50%,#2e1c14)"></div>
  <p class="service-name">Holiday Lighting</p>
</div>
<div class="service-card" style="left:133px;top:1110px">
  <div class="service-photo" role="img" aria-label="Gloved hands cleaning a window with spray and cloth" style="background:radial-gradient(ellipse 60px 80px at 72% 40%,rgba(240,170,50,.8),transparent 70%),radial-gradient(ellipse 90px 70px at 40% 40%,rgba(40,150,210,.75),transparent 70%),linear-gradient(135deg,#5a7a5a,#7fae6a 50%,#5a6a70)"></div>
  <p class="service-name">Window Cleaning</p>
</div>
<div class="service-card" style="left:451px;top:1110px">
  <div class="service-photo" role="img" aria-label="Worker installing insulation in an attic" style="background:radial-gradient(ellipse 50px 100px at 62% 60%,rgba(70,80,110,.6),transparent 70%),radial-gradient(ellipse 80px 60px at 15% 80%,rgba(250,245,235,.8),transparent 70%),linear-gradient(135deg,#b5703a,#d9cbb8 55%,#8a6a4a)"></div>
  <p class="service-name">Insulation Service</p>
</div>
<a class="view-all" href="#" role="img" aria-label="Dimmed lit garden behind a link to all services">View all services</a>

<section class="welcome" role="img" aria-label="Family relaxing together on a sofa at home">
  <div class="welcome-text">
    <p class="welcome-kicker">WELCOME TO</p>
    <h2 class="welcome-title">BRIGHTWAY SERVICES</h2>
    <p class="welcome-body">Lorem Ipsum is simply dummy text of the printing and typesetting industry. Lorem Ipsum has been the industry's standard dummy text ever since the 1500s, when an unknown printer took a galley of type and scrambled it to make a type.</p>
  </div>
</section>

<h2 class="section-title reviews-title">REVIEWS</h2>

<div class="review-card" style="left:133px;top:2128px">
  <div class="review-photo" role="img" aria-label="Garden at dusk with path lights" style="background:radial-gradient(ellipse 70px 50px at 45% 35%,rgba(90,110,80,.7),transparent 70%),radial-gradient(ellipse 40px 30px at 80% 55%,rgba(230,190,110,.6),transparent 70%),linear-gradient(180deg,#2e3a26,#3f5a24 60%,#4c6e26)"></div>
  <p class="review-name">Richard</p>
  <p class="review-text">Lorem Ipsum is simply dummy text of the printing and typesetting industry. Lorem Ipsum has been the industry's standard dummy text ever since the when an unknown printer.</p>
</div>
<div class="review-card" style="left:451px;top:2128px">
  <div class="review-photo" role="img" aria-label="Dark roof tiles and gutter against blue sky" style="background:linear-gradient(160deg,#9cc4e8,#8fb4d8 40%,#2e3640 55%,#3a3e46 75%,#e8e8e4 80%)"></div>
  <p class="review-name">Mark Smith</p>
  <p class="review-text">Lorem Ipsum is simply dummy text of the printing and typesetting industry. Lorem Ipsum has been the industry's standard dummy text ever since the when an unknown printer.</p>
</div>
<div class="review-card" style="left:773px;top:2128px">
  <div class="review-photo" role="img" aria-label="Stone patio with small ground lights at night" style="background:radial-gradient(ellipse 120px 40px at 60% 75%,rgba(220,200,170,.6),transparent 70%),linear-gradient(180deg,#2a2a28,#4a5a3a 35%,#7a7064 60%,#4a4a52)"></div>
  <p class="review-name">Ferando</p>
  <p class="review-text">Lorem Ipsum is simply dummy text of the printing and typesetting industry. Lorem Ipsum has been the industry's standard dummy text ever since the when an unknown printer.</p>
</div>

<section class="cta" role="img" aria-label="Close view of a dark roof gutter at dusk">
  <h2 class="cta-title">LOREM IPSUM IS SIMPLY DUMMY TEXT</h2>
  <a class="cta-link" href="#">CONTACT US</a>
</section>

<footer class="site-footer">
  <nav class="footer-nav">
    <a href="#">HOME</a><a href="#">ABOUT US</a><a href="#">SERVICES</a><a href="#">BLOG</a><a href="#">CONTACT US</a>
  </nav>
  <p class="copyright">Copyright © 2021 All Rights Reserved</p>
</footer>

</body>
</html>
```